Residential Construction Design

I'd like a business card that really explains what we do in residential construction. A big name and number, while the other information can be smaller. Since the logo is made up of grays and a teal color, the background may have to stay white? Maybe a subtle gray.(sending 2 different color schemes of the logo for different background color options) I would like a card that just appears "tough" when you look at it.

Industry/Entity Type

Residential

Contact Information for Business Card

Name and logo which will be provided.(Rex Morton Construction, LLC) Rex Morton -Licensed Contractor, Certified Home Inspector. (555) 214-7730 Email: Rmorton_Construction@quellbox.example -Remodeling -Roofs - Siding -Drywall -Decks -Pole Barns -New Construction "Serving Southwest Michigan"

```html
<!DOCTYPE html>
<html lang="en">
<head>
<meta charset="utf-8">
<title>Rex Morton Construction, LLC — Business Card</title>
<link rel="stylesheet" href="https://fonts.googleapis.com/css2?family=Source+Sans+3:wght@400;600;700&display=swap">
<style>
  :root {
    --page-bg: #e6e2dc;
    --card-white: #ffffff;
    --card-gray: #d2d2d2;
    --band-black: #0b0b0b;
    --ink: #141414;
    --ink-soft: #2a2a2a;
    --brand-ink: #3a3a3a;
    --mark-gray: #6b6b6b;
    --divider: #555555;
    --band-divider: #8a8a8a;
    --band-text: #ffffff;
  }
  * { box-sizing: border-box; margin: 0; padding: 0; }
  html, body {
    width: 1200px; height: 846px; overflow: hidden;
    background: var(--page-bg);
    font-family: "Source Sans 3", "Myriad Pro", Arial, sans-serif;
  }
  .card {
    position: absolute; left: 100px; top: 117px;
    width: 1000px; height: 612px;
    border-radius: 30px; overflow: hidden;
    background: var(--card-white);
    box-shadow: 0 2px 6px rgba(0,0,0,.18);
  }
  .card-backdrop { position: absolute; inset: 0; width: 1000px; height: 612px; }
  .brand-square {
    position: absolute; left: 250px; top: 58px;
    width: 120px; height: 120px; background: var(--mark-gray);
  }
  .brand-name {
    position: absolute; left: 430px; top: 70px;
    color: var(--brand-ink); font-weight: 700; line-height: 1;
  }
  .brand-name .brand-main { display: block; font-size: 66px; letter-spacing: 1px; }
  .brand-name .brand-sub { display: block; font-size: 29px; letter-spacing: 1px; margin-top: 2px; padding-left: 4px; }
  .contact-person { position: absolute; left: 87px; top: 302px; color: var(--ink); }
  .person-name { font-size: 33px; font-weight: 700; line-height: 1.15; }
  .person-role { font-size: 27px; font-weight: 600; line-height: 1.15; }
  .person-cert { font-size: 21px; font-weight: 400; line-height: 1.2; color: var(--ink-soft); }
  .contact-divider {
    position: absolute; left: 414px; top: 296px;
    width: 1.5px; height: 138px; background: var(--divider);
  }
  .contact-line {
    position: absolute; left: 456px; display: flex; align-items: center; gap: 20px;
    color: var(--ink); font-weight: 600;
  }
  .contact-phone { top: 326px; font-size: 28px; }
  .contact-email { top: 380px; font-size: 22px; }
  .contact-line svg { flex: none; }
  .service-area {
    position: absolute; left: 0; width: 1000px; top: 470px;
    text-align: center; padding-right: 6px;
    font-size: 27px; font-weight: 600; color: var(--ink);
  }
  .service-band {
    position: absolute; left: 0; top: 509px; width: 1000px; height: 103px;
    background: var(--band-black);
    display: flex; justify-content: center; align-items: flex-start; padding-top: 16px;
  }
  .service-item {
    color: var(--band-text); font-size: 24px; font-weight: 600;
    padding: 2px 6px 4px; line-height: 1.3;
  }
  .service-item + .service-item { border-left: 1.5px solid var(--band-divider); }
</style>
</head>
<body>
  <div class="card">
    <svg class="card-backdrop" viewBox="0 0 1000 612" aria-hidden="true">
      <polygon points="0,149 321,270 1000,158 1000,509 0,509" fill="var(--card-gray)"/>
    </svg>

    <div class="brand-square"></div>
    <div class="brand-name">
      <span class="brand-main">Rex Morton</span>
      <span class="brand-sub">CONSTRUCTION, LLC</span>
    </div>

    <div class="contact-person">
      <p class="person-name">Rex Morton</p>
      <p class="person-role">Licensed Contractor</p>
      <p class="person-cert">Certified Home Inspector</p>
    </div>

    <div class="contact-divider"></div>

    <div class="contact-line contact-phone">
      <svg width="30" height="32" viewBox="0 0 30 32" aria-hidden="true">
        <rect x="0" y="0" width="30" height="32" rx="4" fill="var(--ink)"/>
        <path d="M11 7 h5 v6 h-3 q-1 3 0 6 h3 v6 h-5 q-4 -9 0 -18z" fill="#fff"/>
      </svg>
      <span>(555) 214-7730</span>
    </div>

    <div class="contact-line contact-email">
      <svg width="30" height="24" viewBox="0 0 30 24" aria-hidden="true">
        <rect x="1.5" y="1.5" width="27" height="21" rx="2" fill="none" stroke="var(--ink)" stroke-width="3"/>
        <polyline points="2,3 15,14 28,3" fill="none" stroke="var(--ink)" stroke-width="3"/>
      </svg>
      <span>Rmorton_Construction@quellbox.example</span>
    </div>

    <p class="service-area">Serving Southwest Michigan</p>

    <div class="service-band">
      <span class="service-item">Remodeling</span>
      <span class="service-item">Roofs</span>
      <span class="service-item">Siding</span>
      <span class="service-item">Drywall</span>
      <span class="service-item">Decks</span>
      <span class="service-item">Pole Barns</span>
      <span class="service-item">New Construction</span>
    </div>
  </div>
</body>
</html>
```